Cocktail Menu for my Breakfast Cafe

I would like a simple drink menu designed. I have uploaded the info of names and prices as well as our restaurant logo - We are an old meets new kind of theme - lots of antiques in our restaurant with buffalo heads - wood everywhere. I would just like something simple and rustic looking with a modern twist - the colors that I would like are neutral tones - browns/woods / Taupes etc

Target Market(s)

Variety - families and trendy hipsters on the weekend and Business People during the week

Industry/Entity Type

Cafe

Font styles to use
Serif

Colors

Designer to choose colors to be used in the design.

Requirements
Must have
• must fit on 127 X 178 paper - it will be a table tent menu so there will need to be a front and back design - The front should have the entire drink menu and the back can just be a solid color or maybe something with our logo
Nice to have
• Traditional with a modern twist
• Saloon style
• wood motif perhaps?
Should not have
• I'm pretty flexible with ideas

```html
<!DOCTYPE html>
<html lang="en">
<head>
<meta charset="utf-8">
<title>Prairie Cafe – Boozy Breakfast Table Tent</title>
<link rel="stylesheet" href="https://fonts.googleapis.com/css2?family=Rye&family=Oswald:wght@500&family=Fira+Sans:wght@500&display=swap">
<style>
  :root {
    --bg: #d9d6d2;
    --wood-light: #c98a3a;
    --wood-mid: #a8601f;
    --wood-dark: #6b3a16;
    --ink: #0b0908;
    --panel: #050505;
    --cream: #f6f1e8;
  }
  * { box-sizing: border-box; margin: 0; padding: 0; }
  html, body { width: 1200px; height: 905px; overflow: hidden; background: var(--bg); }
  .canvas {
    width: 1200px; height: 905px;
    display: flex; justify-content: center; align-items: center; gap: 30px;
  }
  .card {
    position: relative;
    width: 556px; height: 780px;
    overflow: hidden;
  }
  .wood {
    position: absolute; inset: 0;
    background:
      linear-gradient(90deg, rgba(0,0,0,.12) 0 1px, transparent 1px 100%) 0 0 / 78px 100%,
      radial-gradient(ellipse at 70% 65%, #e3a441 0%, transparent 55%),
      linear-gradient(160deg, var(--wood-mid) 0%, var(--wood-light) 45%, var(--wood-mid) 75%, var(--wood-dark) 100%);
  }

  /* Front (name side) */
  .front .bar {
    position: absolute; left: 74px; right: 74px; height: 34px; background: var(--ink);
  }
  .front .bar.top { top: 0; }
  .front .bar.bottom { bottom: 0; }
  .brand {
    position: absolute; left: 0; right: 0; top: 0; bottom: 0;
    display: flex; align-items: center; justify-content: center; gap: 16px;
    color: var(--ink);
    font-family: "Oswald", sans-serif; font-weight: 500;
    font-size: 52px; letter-spacing: 3px; text-transform: uppercase;
  }
  .brand-dot {
    width: 22px; height: 22px; border-radius: 50%; background: var(--ink);
  }

  /* Back (menu side) */
  .menu-panel {
    position: absolute; top: 40px; bottom: 0; left: 116px; right: 66px;
    background: var(--panel); color: var(--cream);
    padding: 30px 22px 0 20px;
  }
  .menu-title {
    font-family: "Rye", serif; font-weight: 400;
    font-size: 40px; line-height: 1;
  }
  .menu-title span { display: block; border-bottom: 2px solid var(--cream); padding-bottom: 6px; }
  .menu-title .line-1 { width: 190px; }
  .menu-title .line-2 { margin-left: 80px; margin-top: 10px; }
  .menu-list { list-style: none; margin-top: 34px; }
  .drink { margin-bottom: 30px; }
  .drink-name {
    font-family: "Oswald", sans-serif; font-weight: 500;
    font-size: 26px; letter-spacing: 1.5px; text-transform: uppercase; line-height: 1.15;
  }
  .drink-detail {
    font-family: "Fira Sans", sans-serif; font-weight: 500;
    font-size: 16px; line-height: 1.35;
  }
  .price-row { display: flex; justify-content: space-between; font-family: "Fira Sans", sans-serif; font-weight: 500; font-size: 16px; margin-top: 3px; }
  .price { margin-left: 14px; }
</style>
</head>
<body>
<main class="canvas">
  <section class="card front">
    <div class="wood" role="img" aria-label="Weathered amber barn-wood plank background"></div>
    <div class="bar top"></div>
    <h1 class="brand"><span class="brand-dot"></span><span class="brand-name">Prairie Cafe</span></h1>
    <div class="bar bottom"></div>
  </section>

  <section class="card back">
    <div class="wood" role="img" aria-label="Weathered amber barn-wood plank background"></div>
    <div class="menu-panel">
      <h2 class="menu-title"><span class="line-1">Boozy</span><span class="line-2">Breakfast</span></h2>
      <ul class="menu-list">
        <li class="drink">
          <p class="drink-name">Simple Caeser</p>
          <p class="drink-detail">Vodka | Clamora | Worcestershire | Firebrand |<br>Pickled Asparagus</p>
          <p class="price-row"><span>1 oz&nbsp;&nbsp;&nbsp;7.00</span><span>Prairie Size&nbsp;&nbsp;11.00</span></p>
        </li>
        <li class="drink">
          <p class="drink-name">Someone Spiked My Juice!</p>
          <p class="drink-detail">Vodka | Orange Juice</p>
          <p class="price-row"><span>1oz&nbsp;&nbsp;&nbsp;6.00</span><span>Prairie Size&nbsp;&nbsp;10.00</span></p>
        </li>
        <li class="drink">
          <p class="drink-name">Brannagh's 'N Coffee</p>
          <p class="drink-detail">Brannagh's Liqueur | Coffee<span class="price">7.00</span></p>
        </li>
        <li class="drink">
          <p class="drink-name">Madame Mimosa</p>
          <p class="price-row"><span>Prosecco | Orange Juice | Raspberries</span><span>7.00</span></p>
        </li>
        <li class="drink">
          <p class="drink-name">Local Brew</p>
          <p class="drink-detail">Hollow Blonde | Ironbell |<br>Creek Road Organic<span class="price">6.00</span></p>
        </li>
      </ul>
    </div>
  </section>
</main>
</body>
</html>
```